Kestrelvale High School Association Website New Design

We require a fresh new website design for the Kestrelvale High School Old Boys Association. The association is a non-for-profit and as such we like the site to reflect the ethos.
We require a design that uses responsive design techniques, so to allow the site to shift between mobile, tablet and desktop spaces and maintain elements in the site.
We would like a landing/home page design, and also an inner news/article based design included.
We want the site to appeal to a broad market of both the old guard members but also to bring on board the new social savey younger members.
The site needs to have a modern take on a professional yet fresh and opulent/elegant look.
A site that we like influences from is http://www.varonelle-kestra.com/ we especially like the navigation look and feel.
The site needs to be clean and simple to find information and navigate and as such would like the site design elements to reflect this in its layout and element interplay.
This site will act as an information gateway for the member's, but also offer abilities to purchase memberships, get information on up coming events and purchase tickets to these events, and interact with the members on the site.
Hi All designers,
The client has now agreed to make the project funding guaranteed, so I hope to see some great designs from you.
Thanks
Sorry all, I hadn't uploaded the logo, has now been uploaded.
Hi all designers, please don't let the wireframe layout include restrict your design freedom on the page layout. We included this to give you a feel for the elements wanted in the site, but not to push you to have them all in that arrangement. Feel free to move around or remove parts of to make better use of the space.
Also this site is for ex-students who are members of an association linked to the school, and not for the school itself, so your designs need to lean towards a member, events and reunions type site design.
After a review today, client now requires that the sites Events need special consideration. Want to see in a prominent position on the landing page area a good area to showcase the upcoming events. Please take this into consideration in your future design layouts.
Hi All Designers, I appreciate all the new and current designs, and sorry a bit behind on the feedback, have been a bit swamped on my own workload, I will give feedback to you all, and will maybe look at an extension of the deadline if need be, as to also allow the clients to look over designs.
Thanks
Reason: Extending the project deadline to allow more feedback to be provider to all designers, to allow review by clients and the feedback through myself.
Reason: Client was un-available for comment, and want them to be able to give feedback to designers for last round updates.
Reason: Sorry all, client has been overseas, and will only be back next week, so need to extend the deadline to allow for client input next week.
Reason: Sorry client has be delayed overseas, so when be needing to work through the designs next week to allow full ability to give all designs due recognition.
Reason: Waiting for client to review designs.
Target Market(s)
Professionals from all varity of job types
Industry/Entity Type
Events
Requirements
Must have
- Please use the attached Logo in the design and look to use the current colour pallet as much as possible, but open to colour and pallet additions or amendments.
Must have a “hero” header image scroller for ability to showcase upcoming events and other items (Required for home/landing pages, could be amended or removed on inner pages).
Should look to follow the include wire frame layout concept as a good conception starting point - but do not limit to just this layout, use design discretion.
Include prominently positioned events area in layout for upcoming events to push the events heavy aspect of the site.
Should include icons/link abilities to access social sites and applications. Ie Chatterloop etc.
Nice to have
- A modern look with an edge to it.
Creative use of the sites colour pallet and site elements.
Should not have
- should not be a copy of the wireframe with colour added

```html
<!DOCTYPE html>
<html lang="en">
<head>
<meta charset="utf-8">
<title>Kestrelvale High School Old Boys Association – Home</title>
<link href="https://fonts.googleapis.com/css2?family=PT+Sans:ital,wght@0,400;0,700;1,400&family=Ubuntu:wght@300;500&family=Ubuntu+Condensed&display=swap" rel="stylesheet">
<style>
:root{
  --ink:#000;
  --page:#e4e4e4;
  --strip:#e9e9e9;
  --gold:#a3844a;
  --red:#c4232b;
  --red-dark:#8e1318;
  --text:#4a4a4a;
  --white:#fff;
  --rule:#b9b9b9;
  --foot-top:#4b4f55;
  --foot-bottom:#050505;
}
*{box-sizing:border-box;margin:0;padding:0}
html,body{width:1182px;height:1200px;overflow:hidden;background:var(--page)}
body{font-family:"PT Sans",sans-serif;color:var(--text)}
.stage{position:absolute;left:0;top:0;width:1295px;height:1315px;transform:scale(.91274);transform-origin:0 0;overflow:hidden;background:var(--page)}
.abs{position:absolute}
.brand{font-family:"PT Sans",sans-serif;font-weight:700;color:var(--white);letter-spacing:-1px;display:flex;align-items:center;gap:10px;line-height:1}
.brand .mark{width:12px;height:12px;background:var(--red)}
.nav{display:flex;font-weight:700;color:var(--white);font-size:13px}
.nav span{position:absolute;white-space:nowrap}
.nav span::after{content:" »";color:var(--white);font-size:10px}
.rule{position:absolute;height:2px;background:linear-gradient(90deg,transparent,var(--rule) 15%,var(--rule) 85%,transparent)}
.hero{border:2px solid #222;overflow:hidden}
.hero .photo{position:absolute;inset:0;background:linear-gradient(180deg,#b8c7d6 0%,#8a8f8c 40%,#5d5a55 60%,#4e6b3a 80%,#6c8a4a 100%)}
.hero svg{position:absolute;inset:0}
.hero-title{font-family:"Ubuntu Condensed",sans-serif;font-weight:400;color:var(--white);text-shadow:0 2px 3px rgba(0,0,0,.6);text-transform:uppercase;line-height:1;white-space:nowrap}
.hero-copy{color:var(--white);text-shadow:0 1px 2px rgba(0,0,0,.7)}
.btn{position:absolute;border-radius:22px;background:linear-gradient(180deg,#d8303a,var(--red-dark));color:var(--white);display:flex;align-items:center;box-shadow:0 2px 4px rgba(0,0,0,.4)}
.btn i{position:absolute;border-radius:50%;background:var(--white)}
.btn i::after{content:"";position:absolute;left:50%;top:50%;transform:translate(-40%,-50%);border-left:7px solid var(--red);border-top:5px solid transparent;border-bottom:5px solid transparent}
.section-title{font-family:"Ubuntu",sans-serif;font-weight:300;color:var(--gold);text-transform:uppercase;white-space:nowrap}
.tag{position:absolute;background:var(--red);color:var(--white);font-family:"Ubuntu",sans-serif;font-weight:300;text-align:center;text-transform:uppercase;border-bottom:1px solid #7b1016}
.shot{position:absolute;border:2px solid #333;box-shadow:0 3px 6px rgba(0,0,0,.4)}
.shot.band{background:linear-gradient(180deg,#4f6a64 0%,#3a2d25 45%,#5b3f2a 100%)}
.shot.hall{background:linear-gradient(180deg,#6e5a80 0%,#2b2a2c 40%,#2a2824 100%)}
.shot.theatre{background:linear-gradient(180deg,#2f5b62 0%,#1f3035 50%,#263238 100%)}
.body-copy{font-size:12px;line-height:15px}
.more{font-size:11px;font-style:italic;text-decoration:underline;color:#222}
.footer{background:linear-gradient(180deg,var(--foot-top),#1a1b1d 55%,var(--foot-bottom))}
.footer h4{position:absolute;font-weight:400;font-size:15px;color:var(--white)}
.footer li{position:absolute;list-style:none;font-size:12px;color:var(--white);white-space:nowrap}
.footer .bullet::before{content:"• ";}
.mobile{position:absolute;left:714px;top:170px;width:528px;height:1145px;background:var(--page);box-shadow:-6px 4px 14px rgba(0,0,0,.35);overflow:hidden}
.social i{position:absolute;width:24px;height:24px;border-radius:3px}
</style>
</head>
<body>
<div class="stage">

  <!-- Desktop layout -->
  <div class="abs" style="left:0;top:0;width:1295px;height:16px;background:var(--strip)"></div>
  <header class="abs" style="left:0;top:16px;width:1295px;height:83px;background:var(--ink)">
    <div class="brand abs" style="left:92px;top:20px;font-size:46px"><span>kvoba</span><span class="mark"></span></div>
    <nav class="nav">
      <span style="left:531px;top:54px">HOME</span>
      <span style="left:610px;top:54px">NEWS</span>
      <span style="left:687px;top:54px">EVENTS</span>
      <span style="left:774px;top:54px">PHOTOS</span>
      <span style="left:865px;top:54px">MEMBERSHIP</span>
      <span style="left:985px;top:54px">CONTACT</span>
    </nav>
  </header>
  <div class="rule" style="left:0;top:122px;width:1295px"></div>

  <section class="hero abs" style="left:89px;top:144px;width:949px;height:355px;box-shadow:0 18px 18px -10px rgba(0,0,0,.4)">
    <div class="photo" role="img" aria-label="School building with lawn and parked cars"></div>
    <svg width="949" height="355" viewBox="0 0 949 355"><polygon points="0,0 612,0 500,355 0,355" fill="rgba(35,36,40,.72)"/><polygon points="612,0 640,0 528,355 500,355" fill="rgba(255,255,255,.25)"/></svg>
    <h1 class="hero-title abs" style="left:24px;top:70px;font-size:33px">The Association of Excellence</h1>
    <p class="hero-copy abs" style="left:25px;top:132px;width:485px;font-size:12px;line-height:20px">Lorem Ipsum is simply dummy text of the printing and typesetting industry. Lorem Ipsum has been the industry's standard dummy text ever since the 1500s, when an unknown printer took a galley of type and scrambled it to make a type specimen book.</p>
    <a class="btn" style="left:22px;top:208px;width:150px;height:41px;font-size:14px;padding-left:17px">Learn more<i style="left:117px;top:10px;width:22px;height:22px"></i></a>
  </section>

  <h2 class="section-title abs" style="left:93px;top:538px;font-size:21px">Welcome to KVOBA</h2>
  <p class="body-copy abs" style="left:95px;top:576px;width:700px;line-height:16px">Lorem Ipsum is simply dummy text of the printing and typesetting industry. Lorem Ipsum has been the industry's standard dummy text ever since the 1500s, when an unknown printer took a galley of type</p>

  <div class="rule" style="left:60px;top:657px;width:680px"></div>
  <div class="tag" style="left:487px;top:657px;width:148px;height:31px;font-size:19px;line-height:31px">Features</div>

  <div class="shot band" style="left:89px;top:724px;width:224px;height:141px" role="img" aria-label="School band performing"></div>
  <div class="shot hall" style="left:329px;top:724px;width:224px;height:141px" role="img" aria-label="Speaker addressing a hall of students"></div>
  <div class="shot theatre" style="left:569px;top:724px;width:224px;height:141px" role="img" aria-label="Audience in a lecture theatre"></div>

  <h3 class="section-title abs" style="left:144px;top:886px;font-size:16px">What we do</h3>
  <h3 class="section-title abs" style="left:382px;top:886px;font-size:16px">Who we are</h3>
  <h3 class="section-title abs" style="left:631px;top:886px;font-size:16px">How we do it</h3>
  <div class="rule" style="left:100px;top:918px;width:200px"></div>
  <div class="rule" style="left:345px;top:918px;width:190px"></div>
  <div class="rule" style="left:588px;top:918px;width:190px"></div>
  <p class="body-copy abs" style="left:96px;top:937px;width:210px">Lorem Ipsum is simply dummy text of the printing and typesetting industry. Lorem Ipsum has been the industry's standard</p>
  <p class="body-copy abs" style="left:343px;top:937px;width:210px">Lorem Ipsum is simply dummy text of the printing and typesetting industry. Lorem Ipsum has been the industry's standard</p>
  <p class="body-copy abs" style="left:586px;top:937px;width:210px">Lorem Ipsum is simply dummy text of the printing and typesetting industry. Lorem Ipsum has been the industry's standard</p>
  <a class="more abs" style="left:96px;top:1005px">read more</a>
  <a class="more abs" style="left:343px;top:1005px">read more</a>
  <a class="more abs" style="left:586px;top:1005px">read more</a>

  <footer class="footer abs" style="left:0;top:1052px;width:1295px;height:263px">
    <h4 style="left:95px;top:18px">Links</h4>
    <h4 style="left:385px;top:19px">Contact Us</h4>
    <ul>
      <li class="bullet" style="left:92px;top:64px">Payments</li>
      <li class="bullet" style="left:92px;top:92px">About us</li>
      <li class="bullet" style="left:92px;top:120px">Contact us</li>
      <li class="bullet" style="left:92px;top:148px">Links</li>
      <li style="left:387px;top:64px">P | (03) 0123 4567</li>
      <li style="left:387px;top:92px">E | info@emailtogohere.com</li>
      <li style="left:387px;top:120px">W | www.yoursitehere.com</li>
      <li style="left:387px;top:148px">P | 53 Your Street to go here</li>
    </ul>
  </footer>

  <!-- Mobile layout -->
  <div class="mobile">
    <div class="abs" style="left:0;top:0;width:528px;height:16px;background:var(--strip)"></div>
    <header class="abs" style="left:0;top:16px;width:528px;height:143px;background:var(--ink)">
      <div class="brand abs" style="left:188px;top:28px;font-size:48px"><span>kvoba</span><span class="mark"></span></div>
      <nav class="nav">
        <span style="left:34px;top:106px">HOME</span>
        <span style="left:101px;top:106px">NEWS</span>
        <span style="left:167px;top:106px">EVENTS</span>
        <span style="left:242px;top:106px">PHOTOS</span>
        <span style="left:321px;top:106px">MEMBERSHIP</span>
        <span style="left:430px;top:106px">CONTACT</span>
      </nav>
    </header>
    <div class="rule" style="left:30px;top:185px;width:470px"></div>

    <section class="hero abs" style="left:24px;top:212px;width:480px;height:179px;box-shadow:0 14px 14px -8px rgba(0,0,0,.4)">
      <div class="photo" role="img" aria-label="School building with lawn and parked cars"></div>
      <svg width="480" height="179" viewBox="0 0 480 179"><polygon points="0,0 308,0 250,179 0,179" fill="rgba(35,36,40,.72)"/><polygon points="308,0 322,0 264,179 250,179" fill="rgba(255,255,255,.25)"/></svg>
      <h1 class="hero-title abs" style="left:12px;top:8px;font-size:27px;line-height:30px">The Association<br>of Excellence</h1>
      <p class="hero-copy abs" style="left:12px;top:78px;width:240px;font-size:11px;line-height:16px">Lorem Ipsum is simply dummy text of the printing and typesetting industry.</p>
      <a class="btn" style="left:12px;top:130px;width:112px;height:31px;font-size:11px;padding-left:13px">Learn more<i style="left:85px;top:7px;width:17px;height:17px"></i></a>
      <div class="abs" style="left:434px;top:157px;width:34px;height:14px;background:#111;color:#fff;font-size:10px;line-height:14px;display:flex;justify-content:space-around">‹ ›</div>
    </section>

    <h2 class="section-title abs" style="left:27px;top:432px;font-size:20px">Welcome to KVOBA</h2>
    <p class="body-copy abs" style="left:27px;top:469px;width:272px;line-height:15.6px">Lorem Ipsum is simply dummy text of the printing and typesetting industry. Lorem Ipsum has been the industry's standard dummy text ever since the 1500s, when an unknown printer took a galley of type . Lorem Ipsum has been the industry's stand-ard dummy text ever since the 1500s.</p>

    <h2 class="section-title abs" style="left:327px;top:432px;font-size:20px">Social</h2>
    <p class="body-copy abs" style="left:328px;top:469px;width:140px;line-height:16px">Please click below icons for updates</p>
    <div class="social">
      <i style="left:328px;top:510px;background:#3b5a9a"></i>
      <i style="left:364px;top:510px;background:#d9d9d9"></i>
      <i style="left:400px;top:510px;background:#2a7bb4"></i>
      <i style="left:436px;top:510px;background:#2d7a52"></i>
      <i style="left:328px;top:540px;background:#5eb8e3"></i>
      <i style="left:364px;top:540px;background:#7b2a93"></i>
    </div>

    <div class="rule" style="left:30px;top:605px;width:470px"></div>
    <div class="tag" style="left:190px;top:605px;width:148px;height:31px;font-size:19px;line-height:31px">Features</div>

    <div class="shot band" style="left:24px;top:672px;width:220px;height:136px" role="img" aria-label="School band performing"></div>
    <h3 class="section-title abs" style="left:278px;top:669px;font-size:16px">What we do</h3>
    <div class="rule" style="left:278px;top:701px;width:200px"></div>
    <p class="body-copy abs" style="left:278px;top:718px;width:210px">Lorem Ipsum is simply dummy text of the printing and typesetting industry. Lorem Ipsum has been the industry's standard</p>
    <a class="more abs" style="left:278px;top:795px">read more</a>

    <div class="shot hall" style="left:24px;top:847px;width:220px;height:136px" role="img" aria-label="Speaker addressing a hall of students"></div>
    <h3 class="section-title abs" style="left:278px;top:844px;font-size:16px">Who we are</h3>
    <div class="rule" style="left:278px;top:876px;width:200px"></div>
    <p class="body-copy abs" style="left:278px;top:893px;width:210px">Lorem Ipsum is simply dummy text of the printing and typesetting industry. Lorem Ipsum has been the industry's standard</p>
    <a class="more abs" style="left:278px;top:970px">read more</a>

    <div class="shot theatre" style="left:24px;top:1022px;width:220px;height:136px" role="img" aria-label="Audience in a lecture theatre facing a projected screen"></div>
    <h3 class="section-title abs" style="left:277px;top:1019px;font-size:16px">How we do it</h3>
    <div class="rule" style="left:278px;top:1051px;width:200px"></div>
    <p class="body-copy abs" style="left:278px;top:1068px;width:210px">Lorem Ipsum is simply dummy text of the printing and typesetting industry. Lorem Ipsum has been the industry's standard</p>
  </div>

</div>
</body>
</html>
```